Business Card Design Project

i have the logo designed.
I require designs for the managing director and the general manager.
we need space for email, and a mobile number.
any other cool stuff/design you guys just let me see what you got.
The managing director card could be black, minimalist, and the cards for the rest of the company could be using the green logo.
it has to impress. transportation market is fragmented, we want to appear professional and sophisticated.
Md: Tarek bani rahim
General manager: omer rahim
clients: procurement heads of contracting companies
Business

```html
<!DOCTYPE html>
<html lang="en">
<head>
<meta charset="utf-8">
<title>Korvanta Business Cards</title>
<link rel="stylesheet" href="https://fonts.googleapis.com/css2?family=Roboto:ital,wght@0,400;0,700;1,700&display=swap">
<style>
  :root {
    --backdrop: #e4e2df;
    --card-white: #ffffff;
    --brand-green: #1b8a3e;
    --band-green: #1f8b43;
    --rule-green: #8cc63f;
    --text-white: #ffffff;
    --web-grey: #7a7a7a;
  }
  * { margin: 0; padding: 0; box-sizing: border-box; }
  html, body {
    width: 1200px; height: 469px; overflow: hidden;
    background: var(--backdrop);
    font-family: "Roboto", Arial, sans-serif;
  }
  .canvas { position: relative; width: 1200px; height: 469px; }
  .card {
    position: absolute; width: 464px; height: 264px;
    background: var(--card-white);
    box-shadow: 0 3px 10px rgba(0,0,0,0.25);
    overflow: hidden;
  }
  .card-front { left: 107px; top: 103px; }
  .card-back { left: 607px; top: 102px; }

  .brand-lockup {
    position: absolute; display: flex; align-items: center; gap: 12px;
    color: var(--brand-green);
  }
  .brand-dot {
    width: 22px; height: 22px; border-radius: 50%;
    background: var(--brand-green);
  }
  .brand-name {
    font-weight: 700; font-size: 42px; letter-spacing: 0.5px; line-height: 1;
  }
  .card-front .brand-lockup { right: 62px; top: 100px; }

  .accent-rule {
    position: absolute; left: 0; top: 176px; width: 100%; height: 4px;
    background: var(--rule-green);
  }
  .contact-band {
    position: absolute; left: 0; top: 182px; width: 100%; height: 82px;
    background: var(--band-green); color: var(--text-white);
  }
  .contact-list { position: absolute; left: 32px; top: 18px; list-style: none; }
  .contact-list li {
    display: flex; align-items: center; gap: 8px;
    font-size: 14px; line-height: 19px;
  }
  .contact-list svg { width: 12px; height: 12px; fill: var(--text-white); }
  .person { position: absolute; right: 37px; top: 18px; text-align: right; }
  .person-name {
    font-weight: 700; font-style: italic; font-size: 17px; letter-spacing: 0.6px;
  }
  .person-title { font-size: 13.5px; margin-top: 4px; }

  .card-back .brand-lockup {
    left: 50%; top: 96px; transform: translateX(-50%);
  }
  .web-address {
    position: absolute; left: 0; width: 100%; top: 173px;
    text-align: center; font-size: 12px; letter-spacing: 6.5px;
    color: var(--web-grey);
  }
</style>
</head>
<body>
<main class="canvas">
  <section class="card card-front">
    <div class="brand-lockup">
      <span class="brand-dot"></span>
      <span class="brand-name">Korvanta</span>
    </div>
    <div class="accent-rule"></div>
    <div class="contact-band">
      <ul class="contact-list">
        <li>
          <svg viewBox="0 0 12 12" aria-hidden="true"><rect x="3" y="0" width="6" height="12" rx="1.2"/><rect x="4" y="1.5" width="4" height="7" fill="#1f8b43"/></svg>
          012.555.0147
        </li>
        <li>
          <svg viewBox="0 0 12 12" aria-hidden="true"><path d="M0 3h12v8H0z"/><path d="M0 3l6 4 6-4" fill="none" stroke="#1f8b43" stroke-width="1.2"/></svg>
          name@korvanta.com
        </li>
      </ul>
      <div class="person">
        <p class="person-name">TAREK BANI RAHIM</p>
        <p class="person-title">Managing Director</p>
      </div>
    </div>
  </section>

  <section class="card card-back">
    <div class="brand-lockup">
      <span class="brand-dot"></span>
      <span class="brand-name">Korvanta</span>
    </div>
    <p class="web-address">www.korvanta.com</p>
  </section>
</main>
</body>
</html>
```